Nourish Each Morning - Greet each Dawn - The freedom to choose and participate in your own path to hea

I have a logo that needs to be turned into a large banner for my website. I want to keep the same font in the uploaded logo image. Now this image could stay at the top of the header kind of where it is now on the web site, It doesn't have to be the main thing on the page. I want this header to be artistic - alive, healthy, joyous - colorful banner that shows wellness, healing, vitality and hope.
If you had a chronic illness and came to my site what would you want to see? You'd want to feel empowered, enlightened, engaged, hopeful and feel the love, right?.
I look forward to getting your creative ideas and designs.

Target Market(s)

People struggling with illness who are looking for a better quality of life. We provide training and education on how to do that. Hope, happiness - healing - Vitality - whole natural foods - mediation - visualization - whole health.

Industry/Entity Type

Health And Wellness

Logo Text

Nourish Each Morning with the koru and with Marisol Fenwick (use the font on the uploaded file)

Requirements
Must have
• I've changed the photos in this order. You can pick up options here:
• https://www.filecrate.example/s/t8kwe2bzlm4rpxa/IMG_5207%20%20high%20resolution.jpg?dl=0
• https://www.filecrate.example/s/gh3nyq7wpcso2ud/IMG_5281%20high%20resolution.jpg?dl=0
• My original logo - Nourish Each Morning - Marisol Fenwick
• "Together we make tragic moments magic moments" Join us (sign up type button)
Nice to have
• Something stunningly simple, classy, inviting, where my message gets across.
• Here's a similar website to mine: http://joelinbrook.example
• I need a link to join up somewhere - with my quote.
• "My tragic moments have become magic moments" Join us (sign up type button)
Should not have
• I do not want other people in the header.
• No crunchy granola feel!
• This is gone mainstream now.

```html
<!DOCTYPE html>
<html lang="en">
<head>
<meta charset="utf-8">
<title>Nourish Each Morning — Marisol Fenwick</title>
<link rel="stylesheet" href="https://fonts.googleapis.com/css2?family=Mulish:wght@400;600&family=Roboto+Condensed:wght@700&display=swap">
<style>
  :root {
    --sky: #dff1f6;
    --mist: #f4fbf2;
    --leaf-light: #c9e98a;
    --leaf: #8fcc3a;
    --leaf-deep: #5da61f;
    --teal: #6db4b8;
    --royal: #1c3f9e;
    --slate: #5a5a5a;
    --button-top: #3f9df0;
    --button-bottom: #0a56c2;
    --button-ring: #bcd7ee;
    --divider: #ffffff;
    --portrait-dark: #2c3a22;
    --portrait-mid: #5d7a3e;
    --portrait-warm: #c99a70;
  }
  html, body {
    margin: 0;
    padding: 0;
    overflow: hidden;
    background: #ffffff;
  }
  .banner {
    position: relative;
    width: 1200px;
    height: 440px;
    overflow: hidden;
    font-family: "Mulish", sans-serif;
  }
  .banner__backdrop {
    position: absolute;
    inset: 0;
    background:
      radial-gradient(ellipse 420px 260px at 170px 60px, rgba(255,255,255,0.95), rgba(255,255,255,0) 70%),
      radial-gradient(ellipse 500px 200px at 500px 200px, rgba(255,255,255,0.7), rgba(255,255,255,0) 75%),
      linear-gradient(160deg, var(--sky) 0%, var(--mist) 30%, var(--leaf-light) 58%, var(--leaf) 80%, var(--leaf-deep) 100%);
  }
  .banner__divider {
    position: absolute;
    inset: 0;
    background: var(--divider);
    clip-path: polygon(830px 0, 1200px 0, 1200px 440px, 782px 440px);
  }
  .banner__portrait {
    position: absolute;
    inset: 0;
    background:
      radial-gradient(ellipse 150px 190px at 1060px 150px, var(--portrait-warm), rgba(201,154,112,0) 75%),
      linear-gradient(180deg, var(--portrait-mid) 0%, var(--portrait-dark) 100%);
    clip-path: polygon(838px 0, 1200px 0, 1200px 440px, 790px 440px);
  }
  .headline {
    position: absolute;
    left: 122px;
    top: 92px;
    margin: 0;
    font-weight: 400;
    font-size: 58px;
    line-height: 1;
    color: var(--teal);
    letter-spacing: 0.5px;
    white-space: nowrap;
  }
  .headline__mark {
    font-size: 16px;
    vertical-align: top;
    position: relative;
    top: 4px;
    margin-left: 2px;
  }
  .brand {
    position: absolute;
    left: 124px;
    top: 166px;
    display: flex;
    align-items: center;
    gap: 14px;
  }
  .brand__dot {
    width: 34px;
    height: 34px;
    border-radius: 50%;
    background: var(--teal);
  }
  .brand__name {
    font-weight: 600;
    font-size: 44px;
    line-height: 1;
    color: var(--royal);
    white-space: nowrap;
  }
  .tagline {
    position: absolute;
    left: 124px;
    top: 248px;
    margin: 0;
    font-weight: 600;
    font-size: 25px;
    color: var(--slate);
    white-space: nowrap;
  }
  .join {
    position: absolute;
    left: 306px;
    top: 298px;
    width: 228px;
    height: 56px;
    border-radius: 28px;
    background: var(--button-ring);
    display: flex;
    align-items: center;
    justify-content: center;
    text-decoration: none;
  }
  .join__label {
    width: 218px;
    height: 46px;
    border-radius: 23px;
    background: linear-gradient(180deg, var(--button-top), var(--button-bottom));
    color: #ffffff;
    font-family: "Roboto Condensed", sans-serif;
    font-weight: 700;
    font-size: 22px;
    display: flex;
    align-items: center;
    justify-content: center;
    gap: 6px;
  }
</style>
</head>
<body>
  <header class="banner">
    <div class="banner__backdrop" role="img" aria-label="Soft sunlit meadow with fresh green grass and glowing light"></div>
    <div class="banner__divider"></div>
    <div class="banner__portrait" role="img" aria-label="Portrait of Marisol Fenwick outdoors in front of green foliage"></div>

    <h1 class="headline">Nourish Each Morning<span class="headline__mark">™</span></h1>

    <div class="brand">
      <span class="brand__dot"></span>
      <span class="brand__name">Marisol Fenwick</span>
    </div>

    <p class="tagline">My tragic moments have become Magic moments</p>

    <a class="join" href="#join">
      <span class="join__label">JOIN US NOW
        <svg width="12" height="18" viewBox="0 0 12 18" aria-hidden="true"><path d="M2 2 L9 9 L2 16" fill="none" stroke="#ffffff" stroke-width="3.5" stroke-linecap="square"/></svg>
      </span>
    </a>
  </header>
</body>
</html>
```